fresh noodle packaging

we need to rebrand our existing brand which base for asia market in australia, we need a fresher look which market for more western style.

i attached our existing product, involved two logo, we want to make all design into one brand only, ( Bao Tin instead of noodle quillon)

requirement:
trendy
fresh
economical
" looks" enviromental friendly
cost effective

one design as a signature and represent the company, expect to fit all type of noodle except text and color
Updates

Need extra days to review

Target Market(s)

supermarket e.g vantrel

Requirements
Must have
• remain color from our old packaging

```html
<!DOCTYPE html>
<html lang="en">
<head>
<meta charset="utf-8">
<title>Bao Tin Hokkien Fresh Noodle – Pack Front</title>
<link rel="stylesheet" href="https://fonts.googleapis.com/css2?family=Lato:wght@400;700;900&display=swap">
<style>
  :root {
    --backdrop: #a7a6a7;
    --brand-blue: #0f4c86;
    --brand-red: #c8202c;
    --pack-white: #ffffff;
    --outline-blue: #7fb0e0;
    --halal-yellow: #f4c430;
    --aus-green: #1f7a3a;
    --food-warm: #c98a4a;
    --food-deep: #6e4220;
  }
  html, body {
    margin: 0;
    padding: 0;
    width: 1200px;
    height: 2189px;
    overflow: hidden;
    background: var(--backdrop);
  }
  .pack-front {
    position: absolute;
    left: 50px;
    top: 336px;
    width: 1100px;
    height: 1516px;
    display: block;
  }
  .pack-front text { font-family: 'Lato', sans-serif; }
  .brand-name { font-weight: 700; font-size: 19px; fill: var(--pack-white); }
  .variety-name { font-weight: 400; font-size: 50px; fill: none; stroke: var(--outline-blue); stroke-width: 1.4; letter-spacing: -1px; }
  .hero-title { font-weight: 900; font-size: 52px; fill: var(--pack-white); letter-spacing: -1px; }
  .claim-main { font-weight: 400; font-size: 19px; fill: var(--pack-white); }
  .claim-storage { font-weight: 700; font-size: 10.5px; fill: var(--pack-white); }
  .icon-label { font-weight: 900; font-size: 11px; fill: var(--brand-blue); }
  .icon-number { font-weight: 900; font-size: 22px; fill: var(--pack-white); }
  .icon-ring-text { font-weight: 700; font-size: 7.5px; fill: var(--pack-white); letter-spacing: 0.5px; }
  .contact-brand { font-weight: 700; font-size: 7px; fill: var(--pack-white); }
  .contact-line { font-weight: 700; font-size: 5.6px; fill: var(--pack-white); }
  .net-weight { font-weight: 900; font-size: 17px; fill: var(--brand-red); }
</style>
</head>
<body>
<svg class="pack-front" viewBox="0 0 492 678" xmlns="http://www.w3.org/2000/svg" aria-label="Bao Tin hokkien fresh noodle pack front">
  <defs>
    <linearGradient id="foodTone" x1="0" y1="0" x2="1" y2="1">
      <stop offset="0" stop-color="var(--food-warm)"/>
      <stop offset="1" stop-color="var(--food-deep)"/>
    </linearGradient>
    <path id="cookArcTop" d="M197,345 A25,25 0 0 1 247,345"/>
    <path id="cookArcBottom" d="M194,347 A28,28 0 0 0 250,347"/>
  </defs>

  <rect class="pack-base" width="492" height="678" fill="var(--pack-white)"/>

  <path class="red-sweep" d="M0,0 H304 C268,60 262,140 298,210 C340,295 368,390 368,485 C366,565 344,630 318,678 H0 Z" fill="var(--brand-red)"/>
  <path class="blue-panel" d="M0,0 H256 C230,60 226,130 260,200 C300,280 346,380 350,480 C352,560 330,630 300,678 H0 Z" fill="var(--brand-blue)"/>

  <path class="window-frame" d="M292,14 H448 Q475,14 475,42 V628 Q475,655 448,655 H330" fill="none" stroke="var(--brand-red)" stroke-width="5"/>
  <path class="window-inner-line" d="M362,430 C370,520 362,590 334,655" fill="none" stroke="var(--brand-red)" stroke-width="3"/>

  <path class="serving-photo" role="img" aria-label="Plate of stir-fried hokkien noodles with chicken, bean sprouts and coriander"
        d="M0,555 C55,495 180,458 345,445 C350,540 338,620 312,678 H0 Z" fill="url(#foodTone)"/>

  <rect class="brand-box" x="28" y="42" width="184" height="34" rx="4" fill="none" stroke="var(--pack-white)" stroke-width="1.2"/>
  <text class="brand-name" x="120" y="66" text-anchor="middle">Bao Tin Food MFG</text>

  <text class="variety-name" x="30" y="138">hokkien</text>

  <path class="hero-banner" d="M0,150 H252 C268,200 285,250 310,302 H0 Z" fill="var(--brand-red)"/>
  <text class="hero-title" x="28" y="224">FRESH</text>
  <text class="hero-title" x="28" y="274">NOODLE</text>

  <circle class="cert-badge" cx="60" cy="347" r="27" fill="var(--pack-white)"/>
  <circle cx="60" cy="347" r="22" fill="none" stroke="var(--brand-blue)" stroke-width="2"/>

  <path class="low-fat-heart" d="M142,372 L114,344 C104,333 110,318 124,318 C132,318 138,323 142,329 C146,323 152,318 160,318 C174,318 180,333 170,344 Z" fill="var(--pack-white)"/>
  <text class="icon-label" x="142" y="349" text-anchor="middle">LOW FAT</text>

  <text class="icon-ring-text"><textPath href="#cookArcTop" startOffset="50%" text-anchor="middle">COOKING TIME</textPath></text>
  <text class="icon-number" x="222" y="353" text-anchor="middle">1</text>
  <text class="icon-ring-text"><textPath href="#cookArcBottom" startOffset="50%" text-anchor="middle">MINUTE</textPath></text>

  <text class="claim-main" x="32" y="418">NO PRESERVATIVES</text>
  <text class="claim-storage" x="32" y="441">KEEP REFRIGERATED AT OR BELOW 4°C</text>

  <circle class="halal-badge" cx="298" cy="463" r="40" fill="var(--halal-yellow)"/>
  <circle cx="298" cy="463" r="30" fill="none" stroke="var(--pack-white)" stroke-width="1.5"/>

  <rect class="origin-badge" x="17" y="600" width="158" height="40" fill="var(--pack-white)" stroke="var(--aus-green)" stroke-width="2"/>
  <rect x="24" y="608" width="24" height="24" fill="var(--aus-green)"/>

  <rect class="contact-block" x="184" y="604" width="160" height="38" rx="2" fill="var(--brand-red)"/>
  <rect x="188" y="609" width="72" height="11" fill="none" stroke="var(--pack-white)" stroke-width="0.8"/>
  <text class="contact-brand" x="224" y="617" text-anchor="middle">Bao Tin Food MFG</text>
  <path class="phone-icon" d="M265,611 l2,0 l1,2 l-1,1 q1,2 3,3 l1,-1 l2,1 l0,2 q-6,0 -8,-8 z" fill="var(--pack-white)"/>
  <text class="contact-brand" x="276" y="618">+61 2 5550 1742</text>
  <text class="contact-line" x="190" y="630">Unit 8, 42-48 Harlow Street</text>
  <text class="contact-line" x="190" y="638">2170 Liverpool, New South Wales, Australia</text>

  <text class="net-weight" x="358" y="636">NET :2Kg</text>
</svg>
</body>
</html>
```